Postcard Design

I need to have a Table Tent made for our Restaurant. On one side is the Burger Specials and the other side is Happy Hour Drink specials. Our colors are black and white in the restaurant. We need a slightly larger font as our customers are older. The cost of the burgers is $13 each. we are an old school steak house.

Restaurant

```html
<!DOCTYPE html>
<html lang="en">
<head>
<meta charset="utf-8">
<title>Burger Specials – Harlow's Steakhouse</title>
<link rel="stylesheet" href="https://fonts.googleapis.com/css2?family=Oswald:wght@500;700&family=Catamaran:wght@500;700;800&display=swap">
<style>
  :root {
    --page: #ffffff;
    --wood-dark: #0f0f0f;
    --wood-mid: #2b2b2b;
    --ribbon: #6e3b22;
    --bar-left: #5a2915;
    --bar-right: #4b311c;
    --badge-ink: #4a2e1a;
    --bun: #d9962f;
    --patty: #5a3215;
    --leaf: #6aa33a;
    --text: #ffffff;
    --text-soft: #f2f2f2;
  }
  * { margin: 0; padding: 0; box-sizing: border-box; }
  html, body { width: 1200px; height: 825px; overflow: hidden; background: var(--page); }
  body { position: relative; font-family: "Catamaran", sans-serif; color: var(--text); }

  .card { position: absolute; left: 12px; top: 10px; width: 1158px; height: 780px; overflow: hidden; }
  .card__backdrop {
    position: absolute; inset: 0;
    background:
      radial-gradient(ellipse at 75% 45%, rgba(90,90,90,.45), transparent 60%),
      linear-gradient(100deg, var(--wood-dark) 0%, var(--wood-mid) 45%, #1c1c1c 70%, var(--wood-dark) 100%);
  }

  .header-ribbon { position: absolute; left: 0; top: 20px; width: 450px; height: 74px; }
  .header-title {
    position: absolute; left: 98px; top: 36px;
    font-family: "Oswald", sans-serif; font-weight: 700; font-size: 33px; letter-spacing: .5px;
    text-shadow: 2px 2px 3px rgba(0,0,0,.5);
  }

  .burger-icon { position: absolute; width: 34px; height: 22px; }
  .burger-icon--lg { width: 48px; height: 30px; }

  .delivery { position: absolute; right: 24px; top: 40px; display: flex; align-items: center; gap: 14px; }
  .delivery__label { font-weight: 800; font-size: 18px; letter-spacing: .5px; margin-right: 2px; }
  .delivery__partner {
    width: 66px; height: 66px; border-radius: 50%; background: var(--page);
    display: flex; align-items: center; justify-content: center;
    color: var(--badge-ink); font-weight: 800; font-size: 14px;
  }

  .specials { position: absolute; left: 98px; top: 118px; list-style: none; }
  .special { height: 116px; }
  .special__name { font-weight: 800; font-size: 27px; line-height: 1.2; letter-spacing: .3px; }
  .special__desc { font-weight: 500; font-size: 19px; line-height: 1.5; color: var(--text-soft); }

  .price-badge {
    position: absolute; left: 903px; top: 430px; width: 220px; height: 220px;
    border-radius: 50%; background: var(--page);
    display: flex; align-items: center; justify-content: center;
  }
  .price-badge__ring {
    width: 194px; height: 194px; border-radius: 50%; border: 4px solid var(--badge-ink);
    text-align: center; color: var(--badge-ink); padding-top: 22px;
  }
  .price-badge__note { font-family: "Oswald", sans-serif; font-weight: 500; font-size: 25px; line-height: 1.15; }
  .price-badge__amount { font-family: "Oswald", sans-serif; font-weight: 700; font-size: 62px; line-height: 1.15; }
  .price-badge__amount sup { font-size: 30px; vertical-align: 22px; }
  .cutlery {
    position: absolute; left: 914px; top: 612px; width: 104px; height: 50px;
    background: linear-gradient(160deg, #efe6d4, #cfc2a8); border-radius: 24px; transform: rotate(12deg);
  }

  .footer-bars { position: absolute; left: 0; bottom: 0; width: 1158px; height: 90px; }
  .footer-phone {
    position: absolute; left: 22px; bottom: 20px;
    font-weight: 800; font-size: 25px; letter-spacing: .4px;
  }
  .footer-web {
    position: absolute; right: 30px; bottom: 26px;
    font-weight: 800; font-size: 25px; letter-spacing: 2.5px;
  }
</style>
</head>
<body>
<main class="card">
  <div class="card__backdrop" role="img" aria-label="Dark weathered wooden table planks photograph"></div>

  <svg class="header-ribbon" viewBox="0 0 450 74" aria-hidden="true">
    <polygon points="0,0 450,0 420,37 450,74 0,74" fill="var(--ribbon)"/>
  </svg>
  <div class="burger-icon burger-icon--lg" style="left:28px;top:44px" role="img" aria-label="Burger icon">
    <svg viewBox="0 0 48 30" width="48" height="30"><rect x="2" y="0" width="44" height="30" rx="10" fill="var(--bun)"/></svg>
  </div>
  <h1 class="header-title">BURGER SPECIALS</h1>

  <div class="delivery">
    <span class="delivery__label">WE DELIVER USING</span>
    <span class="delivery__partner">Dashbite</span>
    <span class="delivery__partner">Runnr</span>
  </div>

  <div class="burger-icon" style="left:30px;top:122px" role="img" aria-label="Burger icon"><svg viewBox="0 0 34 22" width="34" height="22"><rect width="34" height="22" rx="8" fill="var(--bun)"/></svg></div>
  <div class="burger-icon" style="left:30px;top:238px" role="img" aria-label="Burger icon"><svg viewBox="0 0 34 22" width="34" height="22"><rect width="34" height="22" rx="8" fill="var(--bun)"/></svg></div>
  <div class="burger-icon" style="left:30px;top:354px" role="img" aria-label="Burger icon"><svg viewBox="0 0 34 22" width="34" height="22"><rect width="34" height="22" rx="8" fill="var(--bun)"/></svg></div>
  <div class="burger-icon" style="left:30px;top:470px" role="img" aria-label="Burger icon"><svg viewBox="0 0 34 22" width="34" height="22"><rect width="34" height="22" rx="8" fill="var(--bun)"/></svg></div>
  <div class="burger-icon" style="left:30px;top:586px" role="img" aria-label="Burger icon"><svg viewBox="0 0 34 22" width="34" height="22"><rect width="34" height="22" rx="8" fill="var(--bun)"/></svg></div>

  <ul class="specials">
    <li class="special">
      <h2 class="special__name">BBQ BACON BURGER</h2>
      <p class="special__desc">bacon, cheddar, onion rings, bbq sauce, lettuce, tomato, and your choice of side.</p>
    </li>
    <li class="special">
      <h2 class="special__name">GREEN CHILE BURGER</h2>
      <p class="special__desc">mustard, pickles, tomato, onions, american cheese, hatch green chile, and your choice of side</p>
    </li>
    <li class="special">
      <h2 class="special__name">GRILLED CHICKEN BLT</h2>
      <p class="special__desc">(grilled chicken, mozzarella, bacon, lettuce, tomato, mayo, and your choice of side</p>
    </li>
    <li class="special">
      <h2 class="special__name">SHRIMP BROCHETTE</h2>
      <p class="special__desc">pepper jack cheese, jalapeno, bacon, served over dirty rice</p>
    </li>
    <li class="special">
      <h2 class="special__name">NO CARB BURGER</h2>
      <p class="special__desc">Lettuce leaves as your bun, meat patty, cheese if you like, lettuce, tomato,<br>onions, mayo, mustard and your choice of side</p>
    </li>
  </ul>

  <div class="price-badge">
    <div class="price-badge__ring">
      <p class="price-badge__note">burger prices<br>should be</p>
      <p class="price-badge__amount"><sup>$</sup>13</p>
    </div>
  </div>
  <div class="cutlery" role="img" aria-label="Fork and spoon illustration"></div>

  <svg class="footer-bars" viewBox="0 0 1158 90" aria-hidden="true">
    <polygon points="0,26 596,26 530,90 0,90" fill="var(--bar-left)"/>
    <polygon points="596,26 610,26 546,90 530,90" fill="var(--page)"/>
    <polygon points="610,0 1158,0 1158,90 522,90" fill="var(--bar-right)"/>
    <polygon points="596,26 624,0 610,0 584,26" fill="var(--page)" opacity="0"/>
  </svg>
  <p class="footer-phone">CALL US FOR ORDER : +214-555-0147</p>
  <p class="footer-web">WWW.HARLOWSSTEAKHOUSE.COM</p>
</main>
</body>
</html>
```